依頼詳細
◆サイトマップ
01.ホーム
02.当院について
03.医院紹介
04.スタッフ紹介
05.初めての方へ
06.銀歯から自然な白い歯へ
07.歯医者にいけなくなった方へ
08.歯の色を全体的に白くしたい方へ
09.口臭が気になる・歯茎に違和感がある
10.歯並びを整えたい方へ
11.歯が失ってしまった方へ
12.虫歯になってしまった方へ
13.お子様の歯を守りたい方へ
14.求人情報
15.よくあるご質問
16.問い合わせ
17.お知らせ(一覧)
18.お知らせ(詳細)
19.ブログ(一覧)
20.ブログ(詳細)

◆TOPに掲載いただきたいもの
・ヘッダー、ロゴ、営業時間、電話番号
・グローバルナビ
・メインイメージ
・お知らせの新着ボックス
・コンセプト
・強み
・各症状ページへ流入する箇所(サイトマップ06~13の内容)
・その他下層ページ移行用バナー(よくあるご質問、問い合わせ、求人情報)
・ブログの新着ボックス
・グーグルマップ
・フッター(ロゴ、院情報、営業時間、サイトマップ)
※仮で作成したもののためレイアウトの並びはお任せ致します。
ただし、配置してあるコンテンツはすべて含まれるようにしてください。
提案で項目を追加頂く等は参考にさせて頂きたいので大変嬉しいです。

◆デザインについて
・希望するイメージ
知的/清潔な/高級感

・希望デザインカラー
茶系
ベースは白やベージュ系

◆参考URL
https://hirotsudentaloffice.example/
スペースのとり方に高級感を感じとても見やすい印象
TOPのコンテンツ量が少ないと感じる
サイトURL
http://203.0.113.47
ページ数
1ページ
希望イメージ
シンプル 複雑
単色 カラフル
暗い 明るい
日常 高級
遊び心 厳粛
未来的 伝統的
女性的 男性的
希望する色
茶系、ベースは白やベージュ系
納品ファイル
• イラストレーター形式 (.ai)
• フォトショップ形式 (.psd)
補足説明
◆素材について
素材として必要なものがある場合には、Pixmora Stock画像をご使用ください。
その際、通常アセットでダウンロード出来る画像のみを使用してください。
Pixmora Stock以外の素材を使用する際には、
必ず無料で提供いただける物のみご使用ください。
※現在、写真の用意がないのですが、撮影後に差し替える予定です。
イメージとしてPixmora Stock画像を使用して作成ください。

◆ロゴ、外観、内観写真について
下記よりダウンロードしてご使用ください。
https://27.fileport-sample.example/0911-a84c27be5190f3d6e4ab07c2f9d8b3e15
PASS:qvrm
もう少し提案が見たいため、延長させて頂きます。
参考サイトを無視した少し奇抜なアイデアも見てみたいです。
■ 選んだ理由

院内で検討の上、決定致しました。
修正等も快諾いただき大変助かりました。

■ 提案者全員のお礼・コメント

皆様たくさんのご提案ありがとうございました。

```html
<!DOCTYPE html>
<html lang="ja">
<head>
<meta charset="utf-8">
<title>MORISAWA DENTAL</title>
<link rel="stylesheet" href="https://fonts.googleapis.com/css2?family=Noto+Serif+JP:wght@400;500&family=Cormorant+Garamond:wght@500&display=swap">
<style>
:root{
  --brown:#5a3b2c;
  --text:#6b5a50;
  --beige:#efe4d6;
  --accent:#7c2a2a;
  --white:#ffffff;
  --line:#a48a76;
}
*{margin:0;padding:0;box-sizing:border-box}
html,body{width:1200px;height:4004px;overflow:hidden;background:var(--white)}
body{position:relative;font-family:"Noto Serif JP",serif;color:var(--text)}
.hero{position:absolute;left:0;top:0;width:1200px;height:500px;
  background:linear-gradient(100deg,#d9c9b3 0%,#f1e8da 30%,#e8dccb 55%,#cbb597 80%,#a88e70 100%)}
.hero-band{position:absolute;left:0;top:0;width:120px;height:500px;background:rgba(255,255,255,.35)}
.logo{position:absolute;left:14px;top:14px;font-family:"Cormorant Garamond",serif;font-weight:500;
  font-size:30px;letter-spacing:3px;color:var(--white);line-height:1}
.menu-btn{position:absolute;right:0;top:0;width:56px;height:56px;background:var(--accent)}
.menu-btn span{position:absolute;left:16px;width:24px;height:2px;background:var(--white)}
.tagline-band{position:absolute;left:320px;top:196px;width:600px;height:112px;background:rgba(255,255,255,.55)}
.tagline{position:absolute;left:0;width:1200px;top:234px;text-align:center;font-size:34px;color:var(--brown);letter-spacing:3px}
.section-title{position:absolute;left:0;width:1200px;text-align:center;font-size:34px;font-weight:500;color:var(--brown);letter-spacing:2px}
.body-text{position:absolute;left:300px;width:600px;font-size:13px;line-height:27px;text-align:center;letter-spacing:1px}
.photo{position:absolute;width:448px;height:320px}
.card{position:absolute;width:452px;background:var(--beige);padding:44px 34px 0}
.card--left{padding-right:100px}
.card h3{font-size:18px;font-weight:500;color:var(--brown);margin-bottom:14px;letter-spacing:1px}
.card p{font-size:12px;line-height:24px;letter-spacing:1px}
.more{position:absolute;right:34px;bottom:28px;font-size:12px;color:var(--brown);display:flex;align-items:center;gap:16px}
.card--left .more{right:100px}
.more::before{content:"";width:80px;height:1px;background:var(--line)}
</style>
</head>
<body>
<header class="hero" role="img" aria-label="明るい歯科医院の受付と待合室の内観写真">
  <div class="hero-band"></div>
  <div class="logo">MORISAWA DENTAL</div>
  <div class="menu-btn"><span style="top:19px"></span><span style="top:27px"></span><span style="top:35px"></span></div>
  <div class="tagline-band"></div>
  <p class="tagline">最高の治療をあなたに</p>
</header>

<h2 class="section-title" style="top:572px">コンセプト</h2>
<p class="body-text" style="top:668px">テキストが入ります。テキストが入ります。テキストが入ります。テキストが入ります。<br>テキストが入ります。テキストが入ります。テキストが入ります。テキストが入ります。<br>テキストが入ります。テキストが入ります。テキストが入ります。テキストが入ります。<br>テキストが入ります。テキストが入ります。テキストが入ります。テキストが入ります。</p>

<h2 class="section-title" style="top:940px">当院の強み</h2>
<p class="body-text" style="top:1036px">テキストが入ります。テキストが入ります。テキストが入ります。テキストが入ります。<br>テキストが入ります。テキストが入ります。テキストが入ります。テキストが入ります。<br>テキストが入ります。テキストが入ります。テキストが入ります。テキストが入ります。<br>テキストが入ります。テキストが入ります。テキストが入ります。テキストが入ります。</p>

<h2 class="section-title" style="top:1322px">お悩みはありませんか?</h2>

<div class="photo" style="left:180px;top:1448px;background:linear-gradient(135deg,#f4efe9,#d8cfc6)" role="img" aria-label="歯の痛みに悩む女性の写真"></div>
<div class="card" style="left:568px;top:1572px;height:268px">
  <h3>虫歯になってしまった方へ</h3>
  <p>テキストが入ります。テキストが入ります。テキストが入ります。テキストが入ります。テキストが入ります。テキストが入ります。テキストが入ります。テキストが入ります。</p>
  <span class="more">詳しくはこちら</span>
</div>

<div class="card card--left" style="left:180px;top:1988px;height:252px">
  <h3>お子様の歯を守りたい方へ</h3>
  <p>テキストが入ります。テキストが入ります。テキストが入ります。テキストが入ります。テキストが入ります。テキストが入ります。テキストが入ります。テキストが入ります。</p>
  <span class="more">詳しくはこちら</span>
</div>
<div class="photo" style="left:572px;top:2052px;background:linear-gradient(135deg,#e9eef2,#c9c2bb)" role="img" aria-label="子どもの歯を診察する歯科衛生士の写真"></div>

<div class="photo" style="left:180px;top:2528px;background:linear-gradient(135deg,#e6e2de,#c9b6a6)" role="img" aria-label="歯科治療を受ける女性の写真"></div>
<div class="card" style="left:568px;top:2656px;height:264px">
  <h3>歯並びを整えたい方へ</h3>
  <p>テキストが入ります。テキストが入ります。テキストが入ります。テキストが入ります。テキストが入ります。テキストが入ります。テキストが入ります。テキストが入ります。</p>
  <span class="more">詳しくはこちら</span>
</div>

<div class="card card--left" style="left:180px;top:3064px;height:264px">
  <h3>歯の色を全体的に白くしたい方へ</h3>
  <p>テキストが入ります。テキストが入ります。テキストが入ります。テキストが入ります。テキストが入ります。テキストが入ります。テキストが入ります。テキストが入ります。</p>
  <span class="more">詳しくはこちら</span>
</div>
<div class="photo" style="left:572px;top:3132px;height:328px;background:linear-gradient(135deg,#e3eef4,#b9c7cf)" role="img" aria-label="白い歯を見せて微笑む女性の写真"></div>

<div class="photo" style="left:180px;top:3612px;height:324px;background:linear-gradient(135deg,#f3eee9,#ddd2c8)" role="img" aria-label="口元を手で覆う女性の写真"></div>
<div class="card" style="left:568px;top:3736px;height:264px">
  <h3>口臭が気になる・歯茎への違和感がある</h3>
  <p>テキストが入ります。テキストが入ります。テキストが入ります。テキストが入ります。テキストが入ります。テキストが入ります。テキストが入ります。テキストが入ります。</p>
  <span class="more">詳しくはこちら</span>
</div>
</body>
</html>
```